charity helping airline passengers needs web site design

We need a website design (and a logo) for a new charity based in Switzerland. We are helping airline passengers to receive the compensation they are entiteld to by european law from the airlines in cases of delays or denied boarding or cancelled flights. Airlines often try to not pay those compensations so the passengers need assistance in receiving the compensations.

Target Market(s)

Switzerland

Industry/Entity Type

Charity

Logo Text

lindenkrügelhof.ch

Number of Pages Required

1 page

Colors

Designer to choose colors to be used in the design.

```html
<!DOCTYPE html>
<html lang="en">
<head>
<meta charset="utf-8">
<title>Charity Helping Airline Passengers</title>
<link rel="stylesheet" href="https://fonts.googleapis.com/css2?family=Oswald:wght@500;600&family=Roboto:wght@400;500;700&display=swap">
<style>
:root{
  --navy:#252a7c;
  --navy-deep:#1c2064;
  --footer:#1e2240;
  --footer-bar:#171a33;
  --orange:#f0621c;
  --white:#ffffff;
  --text:#555a66;
  --heading:#232637;
}
*{box-sizing:border-box;margin:0;padding:0}
html,body{width:1200px;height:2212px;overflow:hidden}
body{font-family:"Roboto",Arial,sans-serif;color:var(--text);background:var(--white)}
.header{height:64px;background:var(--navy);display:flex;align-items:center;justify-content:space-between;padding:0 40px}
.brand{display:flex;align-items:center;gap:12px;color:var(--white);font-weight:700;font-size:20px;line-height:1.05;text-transform:uppercase;letter-spacing:.5px;white-space:nowrap}
.brand-mark{width:28px;height:28px;border-radius:50%;background:var(--white);flex:none}
.header-actions{display:flex;align-items:center;gap:8px}
.social-box{width:28px;height:28px;background:#3b4199}
.btn{display:inline-block;font-family:"Oswald",sans-serif;font-weight:600;text-transform:uppercase;letter-spacing:1.5px;color:var(--white);background:var(--orange);font-size:14px;padding:6px 16px}
.nav{height:32px;background:var(--orange);display:flex;align-items:center;padding:0 40px;gap:34px}
.nav a{color:var(--white);text-decoration:none;font-size:14px;font-weight:500;text-transform:uppercase}
.hero{height:276px;background:linear-gradient(160deg,#8f949d 0%,#5d626b 45%,#3c3f45 100%);display:flex;flex-direction:column;align-items:center;justify-content:flex-end;padding-bottom:34px;text-align:center}
.hero h1{color:var(--white);font-weight:400;font-size:30px;line-height:1.15;width:480px;margin-bottom:16px}
.hero .btn{background:var(--navy)}
.welcome{height:412px;padding:52px 40px 0;text-align:center}
.welcome h2{font-size:28px;color:var(--heading);font-weight:700;margin-bottom:14px}
.rule{width:80px;height:3px;background:var(--orange);margin:0 auto 22px}
.welcome p{font-size:13px;line-height:1.65;margin:0 auto 18px;width:1080px}
.welcome .btn{background:var(--navy);font-size:13px;padding:6px 16px}
.appeal{background:var(--navy);height:290px;display:flex;justify-content:center;gap:24px;padding:36px 40px}
.appeal-card{width:540px;display:flex;background:var(--navy-deep);border:4px solid var(--white)}
.appeal-photo{width:250px}
.appeal-body{flex:1;display:flex;flex-direction:column;align-items:center;justify-content:center;color:var(--white);text-align:center;padding:20px}
.appeal-body h3{font-family:"Oswald",sans-serif;font-size:46px;line-height:1;text-transform:uppercase;font-weight:600}
.appeal-body p{font-size:16px;margin-top:12px;line-height:1.4}
.latest{height:786px;display:flex;gap:40px;padding:80px 40px 0}
.latest-col{flex:1;text-align:center;height:640px;display:flex;flex-direction:column}
.section-title{display:flex;align-items:center;gap:14px;font-size:22px;font-weight:700;color:var(--heading);margin-bottom:30px}
.section-title::before,.section-title::after{content:"";flex:1;height:2px;background:#bfc1c8}
.news-item{display:flex;gap:20px;text-align:left;margin-bottom:30px}
.news-photo{width:240px;height:175px;flex:none}
.news-date{font-size:12px;color:#888;margin-bottom:6px}
.news-item h4{font-size:15px;color:var(--heading);margin-bottom:8px}
.news-item p{font-size:12.5px;line-height:1.6}
.gallery{display:grid;grid-template-columns:repeat(3,1fr);gap:10px}
.gallery div{height:185px}
.latest .btn{background:var(--navy);font-size:13px;padding:6px 18px;margin:auto auto 0}
.footer{height:352px;background:var(--footer);color:#c9cbd8;position:relative;display:flex;gap:40px;padding:36px 40px 0;font-size:12.5px;line-height:1.7}
.footer h5{color:var(--white);font-size:13px;text-transform:uppercase;margin-bottom:12px;font-weight:700;white-space:nowrap}
.footer .brand{font-size:16px;align-self:flex-start}
.footer .brand-mark{width:24px;height:24px}
.f-col{width:200px}
.subscribe input{display:block;width:230px;height:32px;border:none;padding:0 10px;margin-top:10px;font-size:12px}
.links{display:grid;grid-template-columns:1fr 1fr;column-gap:30px;width:200px}
.socials{display:flex;gap:8px}
.socials .social-box{background:var(--navy)}
.footer-bar{position:absolute;left:0;right:0;bottom:0;height:40px;background:var(--footer-bar);color:#b0b3c4;font-size:11.5px;display:flex;align-items:center;justify-content:space-between;padding:0 40px;text-transform:uppercase}
</style>
</head>
<body>
<header class="header">
  <div class="brand"><span class="brand-mark"></span><span>Charity Helping<br>Airline Passengers</span></div>
  <div class="header-actions"><span class="social-box"></span><span class="social-box"></span><span class="btn">Donate Now</span></div>
</header>
<nav class="nav">
  <a>Home</a><a>About Us</a><a>Passengers</a><a>Volunteers</a><a>Events</a><a>Participation</a><a>News</a><a>Contact Us</a>
</nav>
<section class="hero" role="img" aria-label="Photo of tired travellers waiting with luggage in an airport lounge">
  <h1>Lorem Ipsum Dolor Sit Amet, Consectetur Adipiscing Elit.</h1>
  <span class="btn">Donate Now</span>
</section>
<section class="welcome">
  <h2>Welcome to Charity Helping Airline Passengers</h2>
  <div class="rule"></div>
  <p>Lorem Ipsum is simply dummy text of the printing and typesetting industry. Lorem Ipsum has been the industry's standard dummy text ever since the 1500s, when an unknown printer took a galley of type and scrambled it to make a type specimen book. It has survived not only five centuries, but also the leap into electronic typesetting, remaining essentially unchanged. It was popularised in the 1960s with the release of Letraset sheets containing Lorem Ipsum passages, and more recently with desktop publishing software like Aldus PageMaker including versions of Lorem Ipsum.</p>
  <p>Lorem ipsum dolor sit amet, consectetur adipiscing elit, sed do eiusmod tempor incididunt ut labore et dolore magna aliqua. Ut enim ad minim veniam, quis nostrud exercitation ullamco laboris nisi ut aliquip ex ea commodo consequat.</p>
  <span class="btn">Read More &rsaquo;</span>
</section>
<section class="appeal">
  <div class="appeal-card">
    <div class="appeal-photo" role="img" aria-label="Photo of a jar of coins labelled donate" style="background:linear-gradient(160deg,#c9b48a,#7d6a4c)"></div>
    <div class="appeal-body"><h3>Donate<br>Now</h3><p>All Donations Large and<br>Small, Make a Difference</p></div>
  </div>
  <div class="appeal-card">
    <div class="appeal-photo" role="img" aria-label="Photo of two volunteers embracing" style="background:linear-gradient(160deg,#b7c7d6,#6f7f8c)"></div>
    <div class="appeal-body"><h3>Volunteer<br>Now</h3><p>Can you Give a Day to<br>Change a Life?</p></div>
  </div>
</section>
<section class="latest">
  <div class="latest-col">
    <div class="section-title">Latest News/Blog</div>
    <article class="news-item">
      <div class="news-photo" role="img" aria-label="Photo of a passenger waiting at the departure gate" style="background:linear-gradient(150deg,#aab4c2,#5f6a78)"></div>
      <div><div class="news-date">20/02/2017</div><h4>Lorem ipsum dolor sit amet, consecte.</h4><p>Sed do eiusmod tempor incididunt ut labore et dolore magna aliqua. Ut enim ad minim veniam, quis nostrud exercitation ullamco laboris nisi aliquip.</p></div>
    </article>
    <article class="news-item">
      <div class="news-photo" role="img" aria-label="Photo of travellers queueing at an airline counter" style="background:linear-gradient(150deg,#c2b9a8,#6e6558)"></div>
      <div><div class="news-date">20/02/2017</div><h4>Lorem ipsum dolor sit amet, consecte.</h4><p>Sed do eiusmod tempor incididunt ut labore et dolore magna aliqua. Ut enim ad minim veniam, quis nostrud exercitation ullamco laboris nisi aliquip.</p></div>
    </article>
    <span class="btn">See All &rsaquo;</span>
  </div>
  <div class="latest-col">
    <div class="section-title">Latest Picture/Video</div>
    <div class="gallery">
      <div role="img" aria-label="Photo of volunteers at an event" style="background:linear-gradient(150deg,#9fb3c6,#4f6274)"></div>
      <div role="img" aria-label="Photo of a family at the airport" style="background:linear-gradient(150deg,#d8c2a6,#8a7359)"></div>
      <div role="img" aria-label="Photo of hands forming a heart" style="background:linear-gradient(150deg,#e2a6a0,#9a4f4a)"></div>
      <div role="img" aria-label="Photo of a charity team meeting" style="background:linear-gradient(150deg,#b9c4a8,#66704f)"></div>
      <div role="img" aria-label="Photo of passengers in a terminal hall" style="background:linear-gradient(150deg,#a9b9d0,#55637a)"></div>
      <div role="img" aria-label="Photo of a volunteer helping a traveller" style="background:linear-gradient(150deg,#d1b59a,#7b604a)"></div>
    </div>
    <span class="btn">See All &rsaquo;</span>
  </div>
</section>
<footer class="footer">
  <div class="brand"><span class="brand-mark"></span><span>Charity Helping<br>Airline Passengers</span></div>
  <div class="f-col"><h5>Contact Us</h5><p>1024 Lindenweg 12<br>8000 Musterstadt<br><br>Phone: 000 000 00 00<br>Email: info@passagierhilfe-muster.ch</p></div>
  <div class="subscribe"><h5>Subscribe to our Newsletter</h5><p>Lorem ipsum dolor sit amet, conse ctetur<br>adipiscing elit.</p><input type="text" placeholder="Enter your email"></div>
  <div><h5>Quick Links</h5><div class="links"><span>Home</span><span>Events</span><span>About Us</span><span>Participation</span><span>Passengers</span><span>News</span><span>Volunteers</span><span>Contact Us</span></div></div>
  <div><h5>Connect With Us</h5><div class="socials"><span class="social-box"></span><span class="social-box"></span></div></div>
  <div class="footer-bar"><span>&copy; 2017 Charity Helping</span><span>Privacy &amp; Cookies Policy</span></div>
</footer>
</body>
</html>
```